Visual consulting framework

Tamsworth Advisory is a financial consulting business that takes it clients on the following journey:
1. Get fit (disciplined)
2. Get funded (access to capital)
3. Get big (grow)
4. Get out (exit with wealth)
Over thirty years we have identified that the key to being successful on this journey are the following elements or components.
1. Vision
2. Strategy
3. Structure
4. Product & services
5. Sales and marketing
6. System and processes
7. People
8. Culture
9. Finance
10. M&A
11. Performance monitoring
12. Risk management
We require a visual representation of these elements and the journey to communicate to clients and prospects in marketing material.

```html
<!DOCTYPE html>
<html lang="en">
<head>
<meta charset="utf-8">
<title>Tamsworth Advisory – Consulting Framework</title>
<link rel="stylesheet" href="https://fonts.googleapis.com/css2?family=Bebas+Neue&family=Montserrat:wght@400;600;700&display=swap">
<style>
  :root {
    --orange: #f7901e;
    --blue: #09a9ea;
    --ink: #3a3a3a;
    --page: #ececec;
    --card: #ffffff;
    --orbit: #b9b9b9;
    --ring-light: #e5e5e5;
    --centre: #e9e9e9;
  }
  html, body {
    margin: 0;
    width: 800px;
    height: 1200px;
    overflow: hidden;
    background: var(--page);
  }
  .framework-card {
    position: absolute;
    left: 10px;
    top: 299px;
    width: 780px;
    height: 602px;
    display: block;
  }
  .card-bg { fill: var(--card); }
  .header-band { fill: var(--orange); }
  .header-rule { fill: none; stroke: var(--blue); stroke-width: 7; }
  .purpose-line { font-family: "Bebas Neue", "Oswald", sans-serif; font-size: 48px; fill: #fff; }
  .brand-dot { fill: var(--orange); }
  .brand-name { font-family: "Montserrat", sans-serif; font-weight: 400; font-size: 27px; fill: var(--blue); letter-spacing: 1px; }
  .footer-orange { fill: var(--orange); }
  .footer-blue { fill: var(--blue); }
  .orbit { fill: none; stroke: var(--orbit); stroke-width: 3.5; stroke-linecap: round; stroke-dasharray: 0.1 8; }
  .journey-arrow { fill: none; stroke: var(--orbit); stroke-width: 2.5; stroke-dasharray: 5 5; }
  .arrow-head { fill: var(--orbit); }
  .stage-label { font-family: "Bebas Neue", "Oswald", sans-serif; font-size: 40px; fill: var(--ink); }
  .segment-orange { fill: var(--orange); }
  .segment-blue { fill: var(--blue); }
  .element-label { font-family: "Montserrat", sans-serif; font-weight: 600; font-size: 17px; fill: #fff; text-anchor: middle; }
  .element-icon { fill: none; stroke: #fff; stroke-width: 2; stroke-linecap: round; stroke-linejoin: round; }
  .inner-ring { fill: var(--ring-light); }
  .shade { fill: none; stroke-width: 66; stroke-dasharray: 74.87 824; }
  .centre-disc { fill: var(--centre); }
  .centre-title { font-family: "Bebas Neue", "Oswald", sans-serif; font-size: 56px; fill: var(--ink); text-anchor: middle; }
  .milestone-dot { fill: var(--blue); }
  .connector { stroke: #555; stroke-width: 1.5; }
  .tag-box { fill: var(--orange); }
  .tag-label { font-family: "Montserrat", sans-serif; font-weight: 600; font-size: 18px; fill: #fff; text-anchor: middle; }
</style>
</head>
<body>
<svg class="framework-card" viewBox="0 0 1224 945" xmlns="http://www.w3.org/2000/svg">
  <defs>
    <marker id="arrow-tip" viewBox="0 0 10 10" refX="5" refY="5" markerWidth="5" markerHeight="5" orient="auto">
      <path class="arrow-head" d="M0 0 L10 5 L0 10 Z"/>
    </marker>
  </defs>

  <rect class="card-bg" x="0" y="0" width="1224" height="945"/>

  <!-- header -->
  <path class="header-band" d="M0 0 H1224 V10 H860 C820 10 800 40 780 80 C760 115 740 130 700 130 H0 Z"/>
  <path class="header-rule" d="M0 141 H720 C770 141 790 110 810 75 C830 40 850 25 880 25 H1224"/>
  <text class="purpose-line" x="66" y="66" textLength="589" lengthAdjust="spacingAndGlyphs">OUR PURPOSE IS CLEAR, WE GET COMPANIES</text>
  <text class="purpose-line" x="66" y="112" textLength="637" lengthAdjust="spacingAndGlyphs">AND THEIR FOUNDERS, FIT, FUNDED, BIG AND OUT</text>

  <!-- brand -->
  <circle class="brand-dot" cx="922" cy="92" r="32"/>
  <text class="brand-name" x="972" y="90">TAMSWORTH</text>
  <text class="brand-name" x="972" y="124">ADVISORY</text>

  <!-- journey orbit -->
  <circle class="orbit" cx="612" cy="545" r="340"/>
  <path class="journey-arrow" marker-end="url(#arrow-tip)" d="M303.1 303.5 A392 392 0 0 0 239.2 423.9"/>
  <path class="journey-arrow" marker-end="url(#arrow-tip)" d="M233.3 646.5 A392 392 0 0 0 272.5 741"/>
  <path class="journey-arrow" marker-end="url(#arrow-tip)" d="M990.7 443.5 A392 392 0 0 0 940.9 331.5"/>
  <path class="journey-arrow" marker-end="url(#arrow-tip)" d="M940.9 758.5 A392 392 0 0 0 990.7 646.5"/>

  <text class="stage-label" transform="translate(345 280) rotate(-40)">GET FUNDED</text>
  <text class="stage-label" transform="translate(838 222) rotate(45)">GET FIT</text>
  <text class="stage-label" transform="translate(985 465) rotate(90)">GET OUT</text>
  <text class="stage-label" transform="translate(237 570) rotate(-90)">GET BIG</text>

  <!-- element segments -->
  <path class="segment-orange" d="M428 291.8 A313 313 0 0 1 612 232 L612 352 A193 193 0 0 0 498.6 388.9 Z"/>
  <path class="segment-blue"   d="M612 232 A313 313 0 0 1 796 291.8 L725.4 388.9 A193 193 0 0 0 612 352 Z"/>
  <path class="segment-orange" d="M796 291.8 A313 313 0 0 1 909.7 448.3 L795.6 485.4 A193 193 0 0 0 725.4 388.9 Z"/>
  <path class="segment-blue"   d="M909.7 448.3 A313 313 0 0 1 909.7 641.7 L795.6 604.6 A193 193 0 0 0 795.6 485.4 Z"/>
  <path class="segment-orange" d="M909.7 641.7 A313 313 0 0 1 796 798.2 L725.4 701.1 A193 193 0 0 0 795.6 604.6 Z"/>
  <path class="segment-blue"   d="M796 798.2 A313 313 0 0 1 612 858 L612 738 A193 193 0 0 0 725.4 701.1 Z"/>
  <path class="segment-orange" d="M612 858 A313 313 0 0 1 428 798.2 L498.6 701.1 A193 193 0 0 0 612 738 Z"/>
  <path class="segment-blue"   d="M428 798.2 A313 313 0 0 1 314.3 641.7 L428.4 604.6 A193 193 0 0 0 498.6 701.1 Z"/>
  <path class="segment-orange" d="M314.3 641.7 A313 313 0 0 1 314.3 448.3 L428.4 485.4 A193 193 0 0 0 428.4 604.6 Z"/>
  <path class="segment-blue"   d="M314.3 448.3 A313 313 0 0 1 428 291.8 L498.6 388.9 A193 193 0 0 0 428.4 485.4 Z"/>

  <!-- vision -->
  <g class="element" transform="translate(535 309)">
    <g class="element-icon" transform="translate(0 -26)">
      <circle r="18"/><circle r="11"/><circle r="4"/><path d="M0 0 L20 -20 M14 -22 L20 -20 L22 -14"/>
    </g>
    <text class="element-label" y="32">VISION</text>
  </g>
  <!-- m&a -->
  <g class="element" transform="translate(689 309)">
    <g class="element-icon" transform="translate(0 -26)">
      <circle r="20"/><path d="M-12 7 V-7 L-6 2 L0 -7 V7 M4 7 L9 -7 L14 7 M6 2 H12"/>
    </g>
    <text class="element-label" y="32">M&amp;A</text>
  </g>
  <!-- finance -->
  <g class="element" transform="translate(813 399)">
    <g class="element-icon" transform="translate(0 -26)">
      <ellipse cx="-6" cy="-16" rx="12" ry="4"/><path d="M-18 -16 V8 M6 -16 V-6"/><ellipse cx="-6" cy="-6" rx="12" ry="4"/>
      <circle cx="8" cy="6" r="12"/><path d="M12 1 H6 A2.5 2.5 0 0 0 6 6 H10 A2.5 2.5 0 0 1 10 11 H4 M8 -2 V14"/>
    </g>
    <text class="element-label" y="32">FINANCE</text>
  </g>
  <!-- culture -->
  <g class="element" transform="translate(860 545)">
    <g class="element-icon" transform="translate(0 -26)">
      <rect x="-20" y="-8" width="16" height="16"/><rect x="-4" y="-8" width="16" height="16"/>
      <rect x="-12" y="8" width="16" height="14"/><rect x="4" y="-22" width="16" height="14"/>
    </g>
    <text class="element-label" y="32">CULTURE</text>
  </g>
  <!-- people -->
  <g class="element" transform="translate(813 691)">
    <g class="element-icon" transform="translate(0 -26)">
      <circle cx="-14" cy="-10" r="6"/><circle cx="0" cy="-12" r="7"/><circle cx="14" cy="-10" r="6"/>
      <path d="M-24 12 V4 A9 9 0 0 1 -8 2 M24 12 V4 A9 9 0 0 0 8 2 M-10 16 V6 A10 10 0 0 1 10 6 V16 Z"/>
    </g>
    <text class="element-label" y="32">PEOPLE</text>
  </g>
  <!-- system & processes -->
  <g class="element" transform="translate(689 781)">
    <g class="element-icon" transform="translate(0 -30)">
      <circle r="10"/><circle r="16" stroke-dasharray="6 4"/><circle r="22" stroke-dasharray="10 8"/>
    </g>
    <text class="element-label" y="20">SYSTEM &amp;</text>
    <text class="element-label" y="40">PROCESSES</text>
  </g>
  <!-- sales & marketing -->
  <g class="element" transform="translate(535 781)">
    <g class="element-icon" transform="translate(0 -30)">
      <path d="M-8 4 V-4 M-2 4 V-10 M4 4 V-6 M10 4 V-14 M-12 -8 L8 -20 M3 -21 L8 -20 L7 -15"/>
      <path d="M-22 10 H-8 Q0 10 4 14 H18 M-22 18 H14"/>
    </g>
    <text class="element-label" y="20">SALES &amp;</text>
    <text class="element-label" y="40">MARKETING</text>
  </g>
  <!-- product & services -->
  <g class="element" transform="translate(411 691)">
    <g class="element-icon" transform="translate(0 -30)">
      <path d="M0 -18 L14 -11 V3 L0 10 L-14 3 V-11 Z M-14 -11 L0 -4 L14 -11 M0 -4 V10"/>
      <path d="M-24 14 H-10 Q0 14 4 18 H20"/>
    </g>
    <text class="element-label" y="20">PRODUCT &amp;</text>
    <text class="element-label" y="40">SERVICES</text>
  </g>
  <!-- structure -->
  <g class="element" transform="translate(364 545)">
    <g class="element-icon" transform="translate(0 -26)">
      <path d="M0 -20 L9 -6 H-9 Z M0 -6 V2 M-18 2 H18 M-18 2 V8 M-6 2 V8 M6 2 V8 M18 2 V8"/>
      <rect x="-22" y="8" width="8" height="8"/><rect x="-10" y="8" width="8" height="8"/>
      <rect x="2" y="8" width="8" height="8"/><rect x="14" y="8" width="8" height="8"/>
    </g>
    <text class="element-label" y="32">STRUCTURE</text>
  </g>
  <!-- strategy -->
  <g class="element" transform="translate(411 399)">
    <g class="element-icon" transform="translate(0 -26)">
      <rect x="-20" y="-20" width="40" height="28"/>
      <circle cx="-10" cy="-10" r="4"/><path d="M2 -14 L8 -8 M8 -14 L2 -8 M-12 0 L-6 4 M-6 0 L-12 4 M6 0 L12 4 M12 0 L6 4"/>
      <path d="M-12 8 L-16 20 M12 8 L16 20 M-14 14 H14"/>
    </g>
    <text class="element-label" y="32">STRATEGY</text>
  </g>

  <!-- market leader core -->
  <circle class="inner-ring" cx="612" cy="545" r="193"/>
  <g class="shades">
    <circle class="shade" cx="612" cy="545" r="143" stroke="#dadada" transform="rotate(-90 612 545)"/>
    <circle class="shade" cx="612" cy="545" r="143" stroke="#d0d0d0" transform="rotate(-60 612 545)"/>
    <circle class="shade" cx="612" cy="545" r="143" stroke="#c6c6c6" transform="rotate(-30 612 545)"/>
    <circle class="shade" cx="612" cy="545" r="143" stroke="#bcbcbc" transform="rotate(0 612 545)"/>
    <circle class="shade" cx="612" cy="545" r="143" stroke="#b0b0b0" transform="rotate(30 612 545)"/>
    <circle class="shade" cx="612" cy="545" r="143" stroke="#a2a2a2" transform="rotate(60 612 545)"/>
    <circle class="shade" cx="612" cy="545" r="143" stroke="#949494" transform="rotate(90 612 545)"/>
    <circle class="shade" cx="612" cy="545" r="143" stroke="#858585" transform="rotate(120 612 545)"/>
    <circle class="shade" cx="612" cy="545" r="143" stroke="#737373" transform="rotate(150 612 545)"/>
    <circle class="shade" cx="612" cy="545" r="143" stroke="#626262" transform="rotate(180 612 545)"/>
    <circle class="shade" cx="612" cy="545" r="143" stroke="#4f4f4f" transform="rotate(210 612 545)"/>
    <circle class="shade" cx="612" cy="545" r="143" stroke="#383838" transform="rotate(240 612 545)"/>
  </g>
  <circle class="centre-disc" cx="612" cy="545" r="110"/>
  <text class="centre-title" x="612" y="541">MARKET</text>
  <text class="centre-title" x="612" y="590">LEADER</text>

  <!-- milestones -->
  <circle class="milestone-dot" cx="612" cy="203" r="15"/>
  <circle class="milestone-dot" cx="409" cy="822" r="15"/>
  <circle class="milestone-dot" cx="814" cy="822" r="15"/>

  <line class="connector" x1="339" y1="822" x2="394" y2="822"/>
  <rect class="tag-box" x="131" y="790" width="208" height="62" rx="5"/>
  <text class="tag-label" x="235" y="817">RISK</text>
  <text class="tag-label" x="235" y="836">MANAGEMENT</text>

  <line class="connector" x1="829" y1="822" x2="885" y2="822"/>
  <rect class="tag-box" x="885" y="790" width="208" height="62" rx="5"/>
  <text class="tag-label" x="989" y="817">PERFORMANCE</text>
  <text class="tag-label" x="989" y="836">MONITORING</text>

  <!-- footer -->
  <rect class="footer-orange" x="0" y="930" width="612" height="15"/>
  <rect class="footer-blue" x="612" y="930" width="612" height="15"/>
</svg>
</body>
</html>
```